Business Card

Rallying Pitch ([url removed, login to view]) develops fundraising software for not for profit sporting clubs/teams.

We launched only 12 months ago and ran limited beta testing software to ensure the quality of the software. Coming into the 2018 winter season we are ready to ramp it up.

As we are a new company the business card will need to show that we are trustworthy, a serious business and larger than we look. I am also looking for consistency within the brand.

The major fundraising software we will be running next year will be Forecast Arena ([url removed, login to view]) which is a Tipping Competition for a number of sporting leagues in Australia.

Rallying Pitch is the name of the company that should be the major focus but there should also be a secondary focus on Forecast Arena (both logos are attached). I am happy to see suggestions of how this can work, either front and back differences or a combination, I am looking for suggestions from you.

I am thinking of a secondary catch line for Rallying Pitch which is "Fundraising Software for Grass Roots Sport" which I would like to see incorporated.

Please add the following information (happy to see icons or other ways to display this info)

Name: Dermot Quillane
Mobile: 0400 000 000 (i will give the number to the winner)
email: dermot@[url removed, login to view]
Linked In - [url removed, login to view]
Web - [url removed, login to view]

If it works also having [url removed, login to view]

```html
<!DOCTYPE html>
<html lang="en">
<head>
<meta charset="utf-8">
<title>Rallying Pitch — Business Card</title>
<link href="https://fonts.googleapis.com/css2?family=Oswald:wght@300;400;600;700&family=Roboto+Condensed:ital,wght@0,400;1,700&display=swap" rel="stylesheet">
<style>
  :root{
    --backdrop:#6f6f6f;
    --card:#f1f1f0;
    --ink:#1c1d22;
    --ink-soft:#9a9ba0;
    --ink-mid:#55565b;
    --navy:#1a2a78;
    --green:#8aa82a;
    --rule:#8c8c8c;
  }
  *{margin:0;padding:0;box-sizing:border-box}
  html,body{width:1200px;height:780px;overflow:hidden}
  body{background:var(--backdrop);position:relative;font-family:"Oswald",sans-serif;color:var(--ink)}
  .card{position:absolute;left:357px;width:452px;height:249px;background:var(--card)}
  .card--front{top:104px;display:flex;align-items:center;justify-content:center}
  .card--back{top:408px}

  .brand-mark{display:flex;align-items:center;gap:12px}
  .brand-mark__dot{width:30px;height:30px;border-radius:50%;background:var(--green)}
  .brand-mark__name{font-family:"Oswald",sans-serif;font-weight:700;font-size:40px;color:var(--navy);letter-spacing:.5px}

  .partner-row{position:absolute;top:22px;left:0;width:100%;height:28px}
  .partner{position:absolute;top:0;display:flex;align-items:center;gap:5px;transform:translateX(-50%);
    font-family:"Oswald",sans-serif;font-weight:600;font-size:13px;color:var(--ink);white-space:nowrap}
  .partner--primary{left:169px}
  .partner--secondary{left:304px}
  .partner__square{width:10px;height:10px;background:var(--ink)}
  .partner__circle{width:11px;height:11px;border-radius:50%;background:var(--ink)}

  .person{position:absolute;right:238px;top:92px;text-align:right;line-height:1}
  .person__first{font-weight:300;font-size:24px;color:var(--ink-soft);letter-spacing:.5px}
  .person__last{font-weight:600;font-size:24px;color:var(--ink);margin-top:1px}
  .person__role{font-weight:600;font-size:8px;letter-spacing:.5px;margin-top:3px}

  .divider{position:absolute;left:226px;top:96px;width:1px;height:66px;background:var(--rule)}

  .contacts{position:absolute;left:242px;top:101px;list-style:none}
  .contacts li{display:flex;align-items:center;gap:5px;height:11px;
    font-family:"Roboto Condensed",sans-serif;font-size:8.5px;color:var(--ink-mid);white-space:nowrap}
  .contacts svg{width:8px;height:8px;flex:none}

  .tagline{position:absolute;left:0;width:100%;top:223px;text-align:center;
    font-family:"Roboto Condensed",sans-serif;font-style:italic;font-weight:700;font-size:9.5px;
    letter-spacing:.4px;text-transform:uppercase;color:var(--ink)}
</style>
</head>
<body>

<section class="card card--front">
  <div class="brand-mark">
    <span class="brand-mark__dot"></span>
    <span class="brand-mark__name">Rallying Pitch</span>
  </div>
</section>

<section class="card card--back">
  <div class="partner-row">
    <div class="partner partner--primary"><span class="partner__square"></span>Rallying Pitch</div>
    <div class="partner partner--secondary"><span class="partner__circle"></span>Forecast Arena</div>
  </div>

  <div class="person">
    <div class="person__first">DERMOT</div>
    <div class="person__last">QUILLANE</div>
    <div class="person__role">FOUNDER &amp; CEO</div>
  </div>

  <div class="divider"></div>

  <ul class="contacts">
    <li><svg viewBox="0 0 8 8"><circle cx="4" cy="4" r="4" fill="#55565b"/><path d="M2.6 2.2l.8-.2.4 1-.5.4a3 3 0 0 0 1.3 1.3l.4-.5 1 .4-.2.8c-2 .2-3.6-1.4-3.2-3.2z" fill="#fff"/></svg>0412-555-019</li>
    <li><svg viewBox="0 0 8 8"><circle cx="4" cy="4" r="4" fill="#55565b"/><rect x="2" y="2.7" width="4" height="2.8" fill="none" stroke="#fff" stroke-width=".6"/><path d="M2 2.8l2 1.5 2-1.5" fill="none" stroke="#fff" stroke-width=".6"/></svg>dermot@rallyingpitch.com</li>
    <li><svg viewBox="0 0 8 8"><circle cx="4" cy="4" r="4" fill="#55565b"/><circle cx="4" cy="4" r="2" fill="none" stroke="#fff" stroke-width=".6"/><path d="M2 4h4M4 2v4" stroke="#fff" stroke-width=".5"/></svg>www.rallyingpitch.com</li>
    <li><svg viewBox="0 0 8 8"><circle cx="4" cy="4" r="4" fill="#55565b"/><circle cx="4" cy="4" r="2" fill="none" stroke="#fff" stroke-width=".6"/><path d="M2 4h4M4 2v4" stroke="#fff" stroke-width=".5"/></svg>www.forecastarena.com</li>
    <li><svg viewBox="0 0 8 8"><circle cx="4" cy="4" r="4" fill="#55565b"/></svg>dermotquillane</li>
  </ul>

  <div class="tagline">Fundraising Software for Grass Root Sports</div>
</section>

</body>
</html>
```